Redesign of 3-4 page site for professional services firm

Our site is www.kestrelvaleadvisors.com. We currently have a simple page made with HostNimbo tools. But the tools are not able to generate the look and feel we desire. We need a home page similar to current that tells a little about our company, our experience and our team. We need a second page to show details of current and past transactions we have assisted our clients with. Currently this page reads like a word document but we would like for it to present in a cleaner fashion and liven it up with some images that link to the industry served. For example, a motorcycle outline in a circle for the powersports related transactions. We would like page to introduce each member of "Our Team" and highlight their experience with a photo of each person. If there is no photo available, we would like a placeholder to be their initials in a circle that can be updated later. We would also like a contact us section whether this is a different page or part of the home page.

Target Market(s)

Retirement minded business owners

Industry/Entity Type

Professional Services

Coding

Coded - Design and coding required

Requirements
Must have
• See project description. Must include a page or section for "Current Listings" and "Recently Completed Transactions" (can be same page)

```html
<!DOCTYPE html>
<html lang="en">
<head>
<meta charset="UTF-8">
<title>Kestrel Vale Advisors</title>
<link href="https://fonts.googleapis.com/css2?family=Poppins:wght@400;500;600;700&display=swap" rel="stylesheet">
<style>
:root{
  --purple:#6a2ee8;
  --violet:#7b3ff2;
  --blue:#3f6ef0;
  --green:#22c55e;
  --green-dark:#16a34a;
  --mint:#eaf8ef;
  --ink:#111827;
  --muted:#6b7280;
  --line:#e5e7eb;
  --navy:#0c2236;
  --yellow:#facc15;
  --white:#ffffff;
}
*{box-sizing:border-box;margin:0;padding:0}
html,body{width:1200px;height:4375px;overflow:hidden}
body{font-family:'Poppins',sans-serif;color:var(--ink);background:var(--white);position:relative}
.abs{position:absolute}
.pill{display:inline-block;background:var(--mint);color:var(--green-dark);font-size:11px;font-weight:500;padding:4px 12px;border-radius:20px;border:1px solid #bfe9cd}
.btn{display:inline-block;background:var(--green);color:#fff;font-size:13px;font-weight:500;padding:10px 22px;border-radius:24px;white-space:nowrap}
.center{text-align:center}
h2.section-title{font-size:30px;font-weight:600;color:var(--ink)}

/* hero */
.hero{left:0;top:0;width:1200px;height:500px;background:linear-gradient(115deg,#7a2fe6 0%,#5b3ef0 55%,#3c6ff2 100%)}
.nav{left:0;top:0;width:1200px;height:64px;display:flex;align-items:center;padding:0 120px}
.brand{display:flex;align-items:center;gap:8px;color:#fff;font-weight:600;font-size:18px}
.brand-dot{width:14px;height:14px;border-radius:50%;background:var(--green)}
.nav-links{margin-left:auto;display:flex;gap:26px;align-items:center;font-size:13px;color:#fff}
.nav-links .active{background:var(--yellow);color:var(--ink);padding:4px 12px;border-radius:14px}
.nav-links .btn{padding:7px 16px;font-size:12px}
.hero-badge{left:160px;top:140px;background:rgba(255,255,255,.18);color:#fff;font-size:12px;padding:5px 14px;border-radius:16px}
.hero-title{left:160px;top:175px;width:360px;color:#fff;font-size:40px;line-height:1.17;font-weight:700}
.hero-copy{left:160px;top:330px;width:360px;color:#ece6ff;font-size:12px;line-height:1.6}
.hero .btn{left:160px;top:405px}
.hero-visual{left:640px;top:70px;width:370px;height:280px;border-radius:18px;background:linear-gradient(160deg,rgba(255,255,255,.55),rgba(255,255,255,.15))}

/* features */
.features{left:145px;top:555px;width:910px;height:245px;background:#fff;border-radius:16px;box-shadow:0 10px 30px rgba(30,30,80,.12);padding:28px 40px}
.features h2{font-size:28px;font-weight:600;text-align:center}
.feature-row{display:flex;justify-content:space-around;margin-top:30px}
.feature{width:230px;text-align:center}
.feature-icon{width:52px;height:52px;margin:0 auto 10px;border-radius:50%;background:var(--mint);display:flex;align-items:center;justify-content:center}
.feature h3{font-size:17px;font-weight:600}
.feature p{font-size:11px;color:var(--muted);margin-top:4px}

/* about */
.about-img{left:145px;top:860px;width:375px;height:340px;border-radius:14px;background:linear-gradient(135deg,#1d3a78,#3b6be0 60%,#9cc2ff)}
.about-text{left:590px;top:855px;width:465px}
.about-text h2{font-size:26px;font-weight:600;line-height:1.3;margin:8px 0 10px}
.about-text p{font-size:11.5px;color:var(--muted);line-height:1.6}
.about-cta{margin-top:14px;background:var(--mint);border-radius:12px;padding:12px 16px;display:flex;align-items:center;gap:16px}
.about-cta span:first-child{font-size:11.5px;font-weight:500;flex:1}

/* stats */
.stats{left:145px;top:1270px;width:910px;height:160px;border-radius:16px;background:linear-gradient(100deg,#7a2fe6,#4d55ee);display:flex;align-items:center;justify-content:space-around;color:#fff}
.stat{text-align:center;width:190px}
.stat strong{display:block;font-size:34px;font-weight:700}
.stat b{display:block;font-size:13px;font-weight:600}
.stat small{display:block;font-size:10px;color:#ddd6ff;margin-top:3px}

/* listings */
.listings-head{left:0;top:1510px;width:1200px}
.listings-head h2{margin-top:8px}
.listing{top:1600px;width:285px;height:210px}
.listing-img{width:285px;height:160px;border-radius:12px}
.listing-cap{display:flex;align-items:center;gap:10px;font-size:13px;font-weight:500;margin-top:14px}
.cap-icon{width:26px;height:26px;border-radius:50%;background:var(--mint);border:1px solid #bfe9cd}
.listing-feature{left:457px;top:1600px;width:285px}
.listing-feature .listing-img{height:115px;background:linear-gradient(135deg,#2a3f55,#5b7a8f)}
.listing-card{background:#fff;border-radius:12px;box-shadow:0 8px 22px rgba(0,0,0,.12);padding:14px 16px;margin:-20px 12px 0;position:relative}
.listing-card h3{font-size:14px;font-weight:600}
.listing-card p{font-size:10px;color:var(--muted);margin:6px 0}
.listing-card a{font-size:11px;color:var(--green-dark);font-weight:500;text-decoration:none}
.view-all{left:560px;top:1830px;padding:8px 20px}

/* experience */
.exp-text{left:180px;top:1985px;width:450px}
.exp-text h2{font-size:30px;font-weight:600;margin-bottom:12px}
.exp-text p{font-size:11px;color:var(--muted);line-height:1.65}
.exp-img{left:660px;top:1930px;width:390px;height:310px;border-radius:14px;background:linear-gradient(135deg,#3a2a1e,#8a5a34 55%,#d9a86c)}

/* team */
.team-head{left:0;top:2345px;width:1200px}
.team-head h2{margin-top:10px}
.team-row{left:160px;top:2440px;width:880px;display:flex;justify-content:space-between}
.member{width:200px;height:240px;background:#fff;border-radius:14px;box-shadow:0 8px 22px rgba(0,0,0,.08);text-align:center;padding-top:18px}
.member-photo{width:120px;height:120px;border-radius:50%;margin:0 auto;background:linear-gradient(160deg,#d1d5db,#9ca3af);border:4px solid var(--mint)}
.member h3{font-size:15px;font-weight:600;margin-top:12px}
.member p{font-size:11px;color:var(--muted)}
.socials{display:flex;gap:8px;justify-content:center;margin-top:8px}
.socials i{width:12px;height:12px;border-radius:50%;background:#9ca3af;display:block}

/* reviews */
.reviews-head{left:0;top:2710px;width:1200px}
.reviews-head h2{margin-top:8px}
.reviews{left:160px;top:2795px;width:880px;display:flex;justify-content:space-between}
.review{width:280px;height:165px;background:var(--mint);border-radius:12px;padding:18px 20px;position:relative}
.review p{font-size:10.5px;color:#374151;line-height:1.6;text-align:center}
.reviewer{display:flex;align-items:center;gap:8px;margin-top:18px}
.reviewer i{width:28px;height:28px;border-radius:50%;background:#9ca3af;display:block}
.reviewer b{font-size:11px;font-weight:600;display:block}
.reviewer small{font-size:9px;color:var(--muted)}
.quote{position:absolute;right:22px;bottom:18px;color:var(--green);font-size:40px;font-weight:700;line-height:1}
.dots{left:570px;top:2985px;display:flex;gap:6px}
.dots i{width:8px;height:8px;border-radius:50%;background:#c4b5fd;display:block}
.dots i:first-child{background:var(--purple)}

/* subscribe */
.subscribe{left:0;top:3095px;width:1200px;height:435px;background:linear-gradient(120deg,#0f1b2b 0%,#2b2a33 45%,#6b3b1f 75%,#a35a24 100%)}
.subscribe-box{left:375px;top:3200px;width:450px;height:215px;background:rgba(40,44,58,.82);border-radius:14px;text-align:center;padding:24px 30px;color:#fff}
.subscribe-box h2{font-size:24px;font-weight:600;margin:10px 0 6px;white-space:nowrap}
.subscribe-box p{font-size:10.5px;color:#d1d5db}
.sub-form{display:flex;align-items:center;background:#fff;border-radius:24px;padding:4px 4px 4px 16px;margin:18px auto 0;width:300px}
.sub-form .field{color:#9ca3af;font-size:11px;flex:1;text-align:left}
.sub-form .btn{padding:7px 16px;font-size:11px}

/* contact */
.map{left:160px;top:3620px;width:440px;height:340px;border-radius:12px;background:linear-gradient(135deg,#b9cfe3,#dbe6ee 50%,#c7d9c0)}
.contact{left:650px;top:3620px;width:400px}
.contact h2{font-size:30px;font-weight:600}
.contact > p{font-size:11px;color:var(--muted);line-height:1.6;margin:6px 0 14px}
.info{display:flex;align-items:center;gap:14px;background:#fff;border:1px solid var(--line);border-radius:10px;padding:12px 14px;margin-bottom:10px;box-shadow:0 4px 12px rgba(0,0,0,.05)}
.info-icon{width:38px;height:38px;border-radius:50%;background:var(--green);display:flex;align-items:center;justify-content:center;flex:none}
.info b{font-size:13px;font-weight:600;display:block}
.info span{font-size:11px;color:var(--muted)}

/* footer */
.footer{left:0;top:4010px;width:1200px;height:365px;background:var(--navy);color:#fff;text-align:center}
.footer .brand{justify-content:center;margin-top:90px;font-size:26px}
.footer .brand-dot{width:20px;height:20px}
.footer-links{display:flex;justify-content:center;gap:30px;font-size:14px;margin-top:70px}
.footer-rule{height:1px;background:rgba(255,255,255,.15);width:900px;margin:24px auto 0}
.footer small{display:block;font-size:11px;color:#cbd5e1;margin-top:14px}
</style>
</head>
<body>

<section class="hero abs">
  <nav class="nav abs">
    <div class="brand"><span class="brand-dot"></span>Kestrel Vale</div>
    <div class="nav-links">
      <span class="active">Home</span><span>Business Listings</span><span>Our Team</span><span class="btn">Contact Us</span>
    </div>
  </nav>
  <span class="hero-badge abs">Welcome Kestrel Vale Advisors</span>
  <h1 class="hero-title abs">Strategically Navigating Business Exits</h1>
  <p class="hero-copy abs">With a commitment to integrity, transparency and trusted professionalism, we strive to create a positive and rewarding experience for all our clients.</p>
  <span class="btn abs">Get Started Today</span>
  <div class="hero-visual abs" role="img" aria-label="Phone screens showing business dashboard app"></div>
</section>

<section class="features abs">
  <h2>Unlock the Power of Your Business Data</h2>
  <div class="feature-row">
    <div class="feature"><div class="feature-icon"><svg width="24" height="24" viewBox="0 0 24 24" fill="none" stroke="#16a34a" stroke-width="2"><circle cx="12" cy="12" r="8"/><circle cx="12" cy="12" r="3"/></svg></div><h3>Strategy Planning</h3><p>Setting priorities and aligning business objectives</p></div>
    <div class="feature"><div class="feature-icon"><svg width="24" height="24" viewBox="0 0 24 24" fill="none" stroke="#16a34a" stroke-width="2"><path d="M4 20V10M10 20V4M16 20v-7M22 20H2"/></svg></div><h3>Operational Analysis</h3><p>Identify inefficiencies and optimize</p></div>
    <div class="feature"><div class="feature-icon"><svg width="24" height="24" viewBox="0 0 24 24" fill="none" stroke="#16a34a" stroke-width="2"><circle cx="12" cy="12" r="9"/><path d="M12 7v10M9 10h5a2 2 0 010 4h-5"/></svg></div><h3>Financial Advising</h3><p>Providing expert guidance on managing finances</p></div>
  </div>
</section>

<div class="about-img abs" role="img" aria-label="Glowing upward arrow symbolising business growth"></div>
<section class="about-text abs">
  <span class="pill">About Us</span>
  <h2>Where Your Success Is Our Mission</h2>
  <p>At Kestrel Vale Advisors, our mission is to empower entrepreneurs and business owners by facilitating seamless transactions that lead to mutual success. We understand that selling or acquiring a business can be a complex and emotional journey, which is why we are dedicated to guiding you every step of the way. With a foundation built on integrity, transparency and unmatched professionalism, we strive to create a positive and rewarding experience for all our clients.</p>
  <div class="about-cta"><span>Join Us To Achieve Sustainable Growth And Reach Your Financial Goals With The Right Strategies</span><span class="btn">Get In Touch</span></div>
</section>

<section class="stats abs">
  <div class="stat"><strong>10+</strong><b>Years Of Experience</b><small>Decades of expertise guiding your success</small></div>
  <div class="stat"><strong>150+</strong><b>Projects Successful</b><small>Proven track record of achieving results</small></div>
  <div class="stat"><strong>98%+</strong><b>Client Satisfaction Rate</b><small>Our clients trust us to deliver exceptional value</small></div>
  <div class="stat"><strong>25+</strong><b>Industries Served</b><small>Broad experience across diverse markets</small></div>
</section>

<div class="listings-head abs center"><span class="pill">Current Listings</span><h2 class="section-title">Business Listings</h2></div>
<div class="listing abs" style="left:145px"><div class="listing-img" role="img" aria-label="Business listing photo" style="background:linear-gradient(135deg,#1f2937,#475569)"></div><div class="listing-cap"><span class="cap-icon"></span>Current Business Listings</div></div>
<div class="listing-feature abs"><div class="listing-img" role="img" aria-label="Sales meeting photo"></div><div class="listing-card"><h3>Recently Completed Business Sales</h3><p>With experience built over many years we help owners close with confidence and care.</p><a href="#">Read More</a></div></div>
<div class="listing abs" style="left:770px"><div class="listing-img" role="img" aria-label="Powersports dealership photo" style="background:linear-gradient(135deg,#0f172a,#334155)"></div><div class="listing-cap"><span class="cap-icon"></span>Powersports Dealership</div></div>
<span class="btn view-all abs">View All</span>

<section class="exp-text abs">
  <h2>Our Experience</h2>
  <p>With decades of experience, Kestrel Vale Advisors has proudly assisted numerous clients in successfully navigating the intricate journey of selling their businesses. Our team brings a wealth of knowledge and expertise acquired through years of working closely with entrepreneurs and business owners across diverse industries. We understand the unique challenges and complexities involved in selling a business, from valuation and marketing to negotiations and closing the deal. Our extensive experience allows us to anticipate potential obstacles and proactively find solutions, ensuring a seamless and efficient process for our clients. We take pride in our record of delivering exceptional results and helping our clients achieve their desired outcomes.</p>
</section>
<div class="exp-img abs" role="img" aria-label="Businessman handling money with financial graphics"></div>

<div class="team-head abs center"><span class="pill">Our Team</span><h2 class="section-title">Meet The Experts Behind Your Success</h2></div>
<div class="team-row abs">
  <div class="member"><div class="member-photo" role="img" aria-label="Portrait of Owen Marsh"></div><h3>Owen Marsh</h3><p>CEO</p><div class="socials"><i></i><i></i><i></i></div></div>
  <div class="member"><div class="member-photo" role="img" aria-label="Portrait of Reed Calloway"></div><h3>Reed Calloway</h3><p>Broker</p><div class="socials"><i></i><i></i><i></i></div></div>
  <div class="member"><div class="member-photo" role="img" aria-label="Portrait of Felix Dunmore"></div><h3>Felix Dunmore</h3><p>Broker</p><div class="socials"><i></i><i></i><i></i></div></div>
  <div class="member"><div class="member-photo" role="img" aria-label="Portrait of Ansel Pryor"></div><h3>Ansel Pryor</h3><p>Broker</p><div class="socials"><i></i><i></i><i></i></div></div>
</div>

<div class="reviews-head abs center"><span class="pill">Testimonial</span><h2 class="section-title">Positive Reviews From Our Clients</h2></div>
<div class="reviews abs">
  <div class="review"><p>"The team understood our vision from day one, bringing it to life with incredible creativity and attention to detail."</p><div class="reviewer"><i></i><div><b>Milo Harwick</b><small>Project Manager</small></div></div><span class="quote">”</span></div>
  <div class="review"><p>"The team understood our vision from day one, bringing it to life with incredible creativity and attention to detail."</p><div class="reviewer"><i></i><div><b>Milo Harwick</b><small>Project Manager</small></div></div><span class="quote">”</span></div>
  <div class="review"><p>"The team understood our vision from day one, bringing it to life with incredible creativity and attention to detail."</p><div class="reviewer"><i></i><div><b>Milo Harwick</b><small>Project Manager</small></div></div><span class="quote">”</span></div>
</div>
<div class="dots abs"><i></i><i></i><i></i><i></i></div>

<section class="subscribe abs" role="img" aria-label="Hands using a phone with finance graphics in warm light"></section>
<div class="subscribe-box abs">
  <span class="pill">Newsletter</span>
  <h2>Subscribe For Expert Guidance &amp; News</h2>
  <p>Sign up to hear from us about exciting new opportunities.</p>
  <div class="sub-form"><span class="field">Enter Your Email...</span><span class="btn">Sign Up</span></div>
</div>

<div class="map abs" role="img" aria-label="Street map showing office location"></div>
<section class="contact abs">
  <h2>Contact Us</h2>
  <p>We strive to be an open book with our clients. Have a question about how we can meet your specific needs? Send us a message or give us a call. We're always happy to meet new customers.</p>
  <div class="info"><span class="info-icon"><svg width="18" height="18" viewBox="0 0 24 24" fill="#fff"><path d="M12 2a7 7 0 00-7 7c0 5 7 13 7 13s7-8 7-13a7 7 0 00-7-7zm0 9.5A2.5 2.5 0 1112 6.5a2.5 2.5 0 010 5z"/></svg></span><div><b>Our Location</b><span>418 Harlow Street, Brightwater, Oklahoma 74000, United States</span></div></div>
  <div class="info"><span class="info-icon"><svg width="18" height="18" viewBox="0 0 24 24" fill="#fff"><path d="M6.6 10.8a15 15 0 006.6 6.6l2.2-2.2a1 1 0 011-.25 11.4 11.4 0 003.6.6 1 1 0 011 1V20a1 1 0 01-1 1A17 17 0 013 4a1 1 0 011-1h3.5a1 1 0 011 1c0 1.25.2 2.45.6 3.6a1 1 0 01-.25 1z"/></svg></span><div><b>Our Phone</b><span>405-555-0142</span></div></div>
  <div class="info"><span class="info-icon"><svg width="18" height="18" viewBox="0 0 24 24" fill="none" stroke="#fff" stroke-width="2"><rect x="3" y="5" width="18" height="14" rx="2"/><path d="M3 7l9 6 9-6"/></svg></span><div><b>Email Address</b><span>hello@kestrelvaleadvisors.com</span></div></div>
</section>

<footer class="footer abs">
  <div class="brand"><span class="brand-dot"></span>Kestrel Vale</div>
  <div class="footer-links"><span>Home</span><span>Business Listings</span><span>Our Team</span></div>
  <div class="footer-rule"></div>
  <small>Copyright © 2025 Kestrel Vale Advisors – All Rights Reserved.</small>
</footer>

</body>
</html>
```